Comparison Website Design for Glue Website

Note: We don't have a logo, it's not needed. Just put placeholder.

We would like a website comparing A to B, simple elegant design, simplistic styling. Website is for helping people find the best glue to glue 2 things together. For example, Metal to wood, Metal to rubber, glass to fabric and so on. Select 2 options and be shown the best glue/adhesive for the job.

Purpose of the website:
Allowing someone to pick 2 materials they want to glue together, and showing them the best product for it. We want someone to select 2 materials like "Metal and Rubber". It'll then show the best glues/adhesives from best #1 to #5-10 other ones. The design is simple and doesn't need much detail.

Design rules:
Please design using bootstrap 4 with a modified 1440px width.

We're looking for 4 main pages:
Home Page, Compare Page, Category Page, Product Page.

Target Market(s)

Everyone

Industry/Entity Type

Adhesive

Number of Pages Required

3 page

Font styles to use
Sans Serif

Colors
876aae
b7a5cd
6b449b
e4daeb
fefeff

Requirements
Must have
• We like the following features of these designs:
https://pixelvane.example/shots/6401517-CoverLoom-Dashboard - Main menu with the drop down, this will change depending on the active page. If they are on a metal page they could be shown "glue metal to ___" options. We also like the simple table view in this design under "users" heading.

https://pixelvane.example/shots/6300662-Volt-Sketch-Quotation-Page - The entire colour palette is great! The simplicity of the design is great.

https://pixelvane.example/shots/8593973-Loans-Comparison-UI - The boxes at the top look great, if there was 2 of these with a compare icon between them and above that saying "glue metal to rubber" and it shows an icon/image or metal and glue... The table of products is also good, it has dot points and details which we like.

https://pixelvane.example/shots/4586351-Transfer-Money/attachments/4586351-Transfer-Money?mode=media - The right it shows which 2 products are selected (metal and rubber) for example, on the left it would say "best glue for metal and rubber". This is too detailed though, so it would need to be simplified nicely.

https://linquora.example/ - They do a good job of "comparing" 2 things and displaying integrations well. You can get lots of ideas from them linking A to B similar to what we want to show.

https://www.campaignflowreview.example/leadnest-vs-drivemint/ - This shows a good example of the hero section how it should look.

Features of each page to help you design:
Home Page-
Menu (shown in examples above)
Hero section (colour section) with a centre heading saying "what do you want to glue together" with 2 boxes below to select materials from.
List of most popular searches (metal to rubber, glass to wood, fabric to leather... repeat these to fill space).
List of popular products with basic details about each one (grid format, not list).
FAQs - You choose design for this
Content section (simple design, headings, paragraphs, dotpoints, images...)
Blog section - Simple 3 column grid with an image on top, heading, paragraph, button.

Compare Page-
Showing 2 materials in the colour hero section under or to the right of the heading and paragraph.
Best product (highlighted)
9 other products (list table)
3 column section saying glue (product a to ___) with other product that isn't product b + reverse of this.
Content section

Category page-
heading and breadcrumbs in hero section
Standard product list 1 column on the left with filters, 3 products shown on the right in grid format with basic details on each one.

Product page-
Image left, details on the right.
Keep the image smaller not 50% as we want it to not take up too much space vertically.
Under this put a table where this product ranks for gluing things together. for example #3 for gluing metal to rubber, #1 for glass to wood.
Content section.

Please note, keep this design flat, simple and pretty. We don't need it over-designed or detailed, we simply want a simple functionality website that clearly shows what we're looking for.

```html
<!DOCTYPE html>
<html lang="en">
<head>
<meta charset="utf-8">
<title>Bondwise</title>
<link href="https://fonts.googleapis.com/css2?family=Poppins:wght@500;600;700&family=IBM+Plex+Sans:wght@400;500;600;700&display=swap" rel="stylesheet">
<style>
:root{
  --purple-deep:#4d1a9c;
  --purple:#6b449b;
  --purple-mid:#876aae;
  --purple-soft:#b7a5cd;
  --lilac:#dfd0e8;
  --lilac-pale:#e4daeb;
  --white:#fefeff;
  --ink:#1b1b1f;
  --text:#3a3a3f;
  --line:#c9c9cf;
  --blog-bg:#f3f0f1;
}
*{box-sizing:border-box;margin:0;padding:0}
html,body{width:1200px;height:2866px;overflow:hidden}
body{font-family:"IBM Plex Sans",Arial,sans-serif;color:var(--text);background:var(--white);position:relative}
h1,h2,.brand{font-family:"Poppins",Arial,sans-serif}
.wrap{width:1018px;margin:0 auto;position:relative}
.btn{display:inline-block;background:var(--purple);color:var(--white);font-weight:700;font-size:11px;letter-spacing:.3px;text-transform:uppercase;padding:6px 11px;text-decoration:none}
.section-title{font-size:21px;font-weight:600;color:var(--ink);text-align:center}
.section-title.ruled::after{content:"";display:block;width:30px;height:2px;background:var(--ink);margin:12px auto 0}

/* header / hero */
.hero{height:495px;position:relative;overflow:hidden;background:linear-gradient(120deg,#5a1ea8 0%,#4a189a 45%,#5b1fa6 75%,#6a2ab2 100%)}
.hero-deco{position:absolute;inset:0}
.topnav{position:absolute;top:24px;left:91px;right:92px;display:flex;justify-content:space-between;align-items:center}
.brand{color:var(--white);font-size:22px;font-weight:700}
.menu{display:flex;gap:36px}
.menu a{color:var(--white);font-weight:600;font-size:12.5px;text-decoration:none;letter-spacing:.3px}
.hero h1{position:absolute;top:150px;width:100%;text-align:center;color:var(--white);font-size:29px;font-weight:700}
.pick{position:absolute;top:231px;width:198px;height:174px;background:rgba(200,180,230,.55);color:var(--white);text-align:center}
.pick svg{margin-top:30px}
.pick span{display:block;margin-top:20px;font-weight:600;font-size:16px;letter-spacing:.5px}
.pick.left{left:355px}.pick.right{left:657px}
.swap{position:absolute;left:576px;top:296px}

/* popular */
.popular{height:322px;padding-top:40px}
.search-grid{display:flex;gap:15px;margin-top:60px}
.search-card{position:relative;width:243px;height:138px;border:1px solid var(--line);text-align:center;padding-top:33px}
.search-card .go{position:absolute;top:-15px;left:50%;margin-left:-15px;width:30px;height:30px}
.search-card h3{font-size:14px;font-weight:500;color:var(--ink)}
.search-card p{font-size:11px;line-height:16px;margin-top:10px;padding:0 34px}

/* products */
.products{height:488px;background:var(--lilac);padding-top:40px}
.product-grid{display:flex;gap:15px;margin-top:38px}
.product-card{width:243px;height:328px;background:var(--white);text-align:center;padding-top:18px}
.product-card .shot{width:200px;height:140px;margin:0 auto}
.product-card h3{font-weight:500;font-size:14px;color:var(--ink);margin-top:24px}
.product-card p{font-size:11px;line-height:16px;margin:13px 36px 0}
.product-card .btn{margin-top:14px;font-size:10px}

/* faq */
.faqs{height:454px;background:linear-gradient(90deg,#ececed,#f7f7f8 50%,#ececed);padding-top:48px}
.faq-grid{display:grid;grid-template-columns:466px 466px;column-gap:13px;width:945px;margin:42px auto 0}
.faq-item{height:43px;border:1px solid #8e8e94;background:var(--white);display:flex;align-items:center;justify-content:space-between;padding:0 14px 0 15px;font-size:12px;color:var(--ink);margin-bottom:16px}
.faq-item:nth-child(n+5){margin-bottom:21px}
.faq-item::after{content:"";border:5px solid transparent;border-top:5px solid var(--ink);border-bottom:0}
.faqs .center{text-align:center;margin-top:15px}

/* about */
.about{height:443px;position:relative}
.about-text{position:absolute;left:92px;top:78px;width:450px}
.about-text h2{font-size:21px;font-weight:600;color:var(--ink)}
.about-text h2::after{content:"";display:block;width:28px;height:2px;background:var(--ink);margin-top:12px}
.about-text p{font-size:12.5px;line-height:18.4px;color:var(--ink);margin-top:30px}
.about-text .btn{margin-top:30px;font-size:12px;padding:7px 10px}
.about-photo{position:absolute;left:592px;top:57px;width:516px;height:332px;background:linear-gradient(160deg,#c98a3a,#b16d22 45%,#8a5418 70%,#dfe3dc 71%,#cfd5cc)}

/* blog */
.blog{height:478px;background:var(--blog-bg);padding-top:36px}
.blog-grid{display:flex;gap:14px;margin-top:30px}
.blog-card{width:243px;height:325px;background:var(--white)}
.blog-card .thumb{height:151px}
.blog-card .body{padding:22px 40px 0 26px}
.blog-card h3{font-size:11px;font-weight:500;line-height:18px;color:var(--ink);text-transform:uppercase}
.blog-card p{font-size:11px;line-height:16px;margin-top:7px}
.blog-card .btn{margin-top:12px;font-size:9.5px;padding:5px 9px}

/* footer */
.site-footer{height:186px;background:linear-gradient(120deg,#5a2ea6,#6b3fab 60%,#7a4bb3)}
.site-footer .row1{display:flex;justify-content:space-between;align-items:center;padding-top:40px;height:95px;border-bottom:1px solid rgba(255,255,255,.35)}
.site-footer .menu{gap:37px}
.site-footer .row2{display:flex;justify-content:space-between;align-items:center;padding-top:24px;color:var(--white);font-size:12px}
.follow{display:flex;align-items:center;gap:8px;font-weight:700;font-size:9.5px}
.follow .dot{width:22px;height:22px;border-radius:50%;background:var(--purple-deep)}
.follow span{margin-right:6px}
</style>
</head>
<body>

<header class="hero">
  <svg class="hero-deco" width="1200" height="495" aria-hidden="true">
    <circle cx="440" cy="10" r="55" fill="none" stroke="rgba(255,255,255,.12)" stroke-width="30"/>
    <circle cx="565" cy="28" r="18" fill="rgba(255,255,255,.15)"/>
    <circle cx="311" cy="120" r="7" fill="rgba(255,255,255,.15)"/>
    <circle cx="712" cy="219" r="5" fill="rgba(255,255,255,.15)"/>
    <path d="M1000 0 C1010 160 1120 240 1200 260 L1200 0Z" fill="rgba(255,255,255,.05)"/>
    <path d="M0 420 C120 450 220 480 330 495 L0 495Z" fill="rgba(255,255,255,.06)"/>
    <path d="M900 495 C1000 420 1110 380 1200 370 L1200 495Z" fill="rgba(0,0,0,.06)"/>
  </svg>
  <nav class="topnav">
    <div class="brand">Bondwise</div>
    <div class="menu"><a href="#">HOME</a><a href="#">COMPARE</a><a href="#">CATEGORY</a><a href="#">PRODUCT</a></div>
  </nav>
  <h1>What do you want to glue together</h1>
  <div class="pick left">
    <svg width="72" height="62" viewBox="0 0 72 62" aria-hidden="true">
      <path d="M2 10 L22 2 L50 34 L30 44Z" fill="#fff"/>
      <path d="M34 46 L54 36 L54 10 L62 10 L62 40 L70 40 L70 60 L34 60Z" fill="none" stroke="#fff" stroke-width="4"/>
    </svg>
    <span>METAL</span>
  </div>
  <svg class="swap" width="50" height="50" viewBox="0 0 50 50" aria-hidden="true">
    <path d="M8 22 C8 12 14 10 22 10 L44 10 M38 4 L44 10 L38 16" fill="none" stroke="#fff" stroke-width="3.5" stroke-linecap="round" stroke-linejoin="round"/>
    <path d="M42 28 C42 38 36 40 28 40 L6 40 M12 34 L6 40 L12 46" fill="none" stroke="#fff" stroke-width="3.5" stroke-linecap="round" stroke-linejoin="round"/>
  </svg>
  <div class="pick right">
    <svg width="58" height="66" viewBox="0 0 58 66" aria-hidden="true">
      <rect x="3" y="3" width="52" height="60" fill="none" stroke="#fff" stroke-width="4"/>
      <circle cx="29" cy="33" r="17" fill="none" stroke="#fff" stroke-width="4"/>
      <circle cx="29" cy="33" r="10" fill="none" stroke="#fff" stroke-width="2"/>
    </svg>
    <span>RUBBER</span>
  </div>
</header>

<section class="popular">
  <div class="wrap">
    <h2 class="section-title">List of most popular searches</h2>
    <div class="search-grid">
      <div class="search-card"><svg class="go" viewBox="0 0 30 30"><circle cx="15" cy="15" r="15" fill="#6b449b"/><path d="M13 10 L18 15 L13 20" fill="none" stroke="#fff" stroke-width="1.8"/></svg><h3>Metal to Rubber</h3><p>Lorem ipsum dolor sit amet consectetur adipiscing elit sed do eiusmod tempor incididunt.</p></div>
      <div class="search-card"><svg class="go" viewBox="0 0 30 30"><circle cx="15" cy="15" r="15" fill="#6b449b"/><path d="M13 10 L18 15 L13 20" fill="none" stroke="#fff" stroke-width="1.8"/></svg><h3>Glass to Wood</h3><p>Lorem ipsum dolor sit amet consectetur adipiscing elit sed do eiusmod tempor incididunt.</p></div>
      <div class="search-card"><svg class="go" viewBox="0 0 30 30"><circle cx="15" cy="15" r="15" fill="#6b449b"/><path d="M13 10 L18 15 L13 20" fill="none" stroke="#fff" stroke-width="1.8"/></svg><h3>Fabric to Leather</h3><p>Lorem ipsum dolor sit amet consectetur adipiscing elit sed do eiusmod tempor incididunt.</p></div>
      <div class="search-card"><svg class="go" viewBox="0 0 30 30"><circle cx="15" cy="15" r="15" fill="#6b449b"/><path d="M13 10 L18 15 L13 20" fill="none" stroke="#fff" stroke-width="1.8"/></svg><h3>Rubber to Metal</h3><p>Lorem ipsum dolor sit amet consectetur adipiscing elit sed do eiusmod tempor incididunt.</p></div>
    </div>
  </div>
</section>

<section class="products">
  <div class="wrap">
    <h2 class="section-title ruled">Our Products</h2>
    <div class="product-grid">
      <div class="product-card"><div class="shot" role="img" aria-label="Steel ball bearings" style="background:radial-gradient(ellipse at center,#9a9ca0,#d8d9dc 60%,#fff 75%)"></div><h3>METAL</h3><p>Lorem ipsum dolor sit amet consectetur adipiscing elit sed do eiusmod tempor incididunt.</p><a class="btn" href="#">Read More</a></div>
      <div class="product-card"><div class="shot" role="img" aria-label="Grey rubber sheets" style="background:radial-gradient(ellipse at center,#6e6f73,#9a9b9e 45%,#fff 70%)"></div><h3>RUBBER</h3><p>Lorem ipsum dolor sit amet consectetur adipiscing elit sed do eiusmod tempor incididunt.</p><a class="btn" href="#">Read More</a></div>
      <div class="product-card"><div class="shot" role="img" aria-label="Glass-top wooden coffee table" style="background:radial-gradient(ellipse at center,#4a2e24,#7a5a4c 45%,#fff 72%)"></div><h3>GLASS</h3><p>Lorem ipsum dolor sit amet consectetur adipiscing elit sed do eiusmod tempor incididunt.</p><a class="btn" href="#">Read More</a></div>
      <div class="product-card"><div class="shot" role="img" aria-label="Wooden lattice window frame" style="background:radial-gradient(ellipse at center,#a98f84,#6b3f30 55%,#fff 76%)"></div><h3>WOOD</h3><p>Lorem ipsum dolor sit amet consectetur adipiscing elit sed do eiusmod tempor incididunt.</p><a class="btn" href="#">Read More</a></div>
    </div>
  </div>
</section>

<section class="faqs">
  <h2 class="section-title ruled">FAQs</h2>
  <div class="faq-grid">
    <div class="faq-item">Lorem Ipsum is simply dummy text of the printing?</div>
    <div class="faq-item">Lorem Ipsum is simply dummy text of the printing?</div>
    <div class="faq-item">Lorem Ipsum is simply dummy text of the printing?</div>
    <div class="faq-item">Lorem Ipsum is simply dummy text of the printing?</div>
    <div class="faq-item">Lorem Ipsum is simply dummy text of the printing?</div>
    <div class="faq-item">Lorem Ipsum is simply dummy text of the printing?</div>
    <div class="faq-item">Lorem Ipsum is simply dummy text of the printing?</div>
    <div class="faq-item">Lorem Ipsum is simply dummy text of the printing?</div>
  </div>
  <div class="center"><a class="btn" href="#">View More FAQs</a></div>
</section>

<section class="about">
  <div class="about-text">
    <h2>About Us Bondwise</h2>
    <p>On the other hand, we denounce with righteous indignation and dislike men who are so beguiled and demoralized by the charms of pleasure of the moment, so blinded by desire, that they cannot foresee the pain and trouble that are bound to ensue; and equal blame belongs to those who fail in their duty through weakness of will, which is the same as saying through shrinking from toil and pain. These cases are perfectly simple and easy to distinguish. In a free hour, when our power of choice is untrammelled and when nothing prevents our being able to do what we like best,</p>
    <a class="btn" href="#">Read More</a>
  </div>
  <div class="about-photo" role="img" aria-label="Close-up of a wooden tabletop corner on a white frame"></div>
</section>

<section class="blog">
  <div class="wrap">
    <h2 class="section-title ruled">Latest Blog</h2>
    <div class="blog-grid">
      <div class="blog-card"><div class="thumb" role="img" aria-label="Glass plaque mounted on a concrete wall" style="background:linear-gradient(135deg,#8e8e8e,#b9b9b9 50%,#7b7b7b)"></div><div class="body"><h3>Lorem Ipsum is simply dummy text of the printing</h3><p>Lorem ipsum dolor sit amet conse ctetur adipiscing elit sed do eius mod tempor incididunt.</p><a class="btn" href="#">Read More</a></div></div>
      <div class="blog-card"><div class="thumb" role="img" aria-label="Rolled metal sheet coil" style="background:radial-gradient(circle at 45% 40%,#111 0,#222 14%,#8d8d8d 30%,#cfcfcf 60%,#6e6e6e)"></div><div class="body"><h3>Lorem Ipsum is simply dummy text of the printing</h3><p>Lorem ipsum dolor sit amet conse ctetur adipiscing elit sed do eius mod tempor incididunt.</p><a class="btn" href="#">Read More</a></div></div>
      <div class="blog-card"><div class="thumb" role="img" aria-label="Stacked glass panes" style="background:linear-gradient(135deg,#2b4f5a,#8fc7cf 45%,#3e6e78 70%,#a9d7db)"></div><div class="body"><h3>Lorem Ipsum is simply dummy text of the printing</h3><p>Lorem ipsum dolor sit amet conse ctetur adipiscing elit sed do eius mod tempor incididunt.</p><a class="btn" href="#">Read More</a></div></div>
      <div class="blog-card"><div class="thumb" role="img" aria-label="Spiral of wooden slats" style="background:radial-gradient(circle at 40% 50%,#f2e4d4 0,#b5672c 25%,#5a2c12 55%,#a35a25)"></div><div class="body"><h3>Lorem Ipsum is simply dummy text of the printing</h3><p>Lorem ipsum dolor sit amet conse ctetur adipiscing elit sed do eius mod tempor incididunt.</p><a class="btn" href="#">Read More</a></div></div>
    </div>
  </div>
</section>

<footer class="site-footer">
  <div class="wrap">
    <div class="row1">
      <div class="brand">Bondwise</div>
      <div class="menu"><a href="#">HOME</a><a href="#">COMPARE</a><a href="#">CATEGORY</a><a href="#">PRODUCT</a></div>
    </div>
    <div class="row2">
      <div class="follow"><span>FOLLOW US</span><i class="dot"></i><i class="dot"></i><i class="dot"></i></div>
      <div>Copyright © 2020 All Rights Reserved</div>
    </div>
  </div>
</footer>

</body>
</html>
```